Freelancers in the field of IT security and IT service need a business card design

I need a business card design for my company. I am a freelancer and active in the area of IT security, IT support% 26 # 252; tung, consulting. I am not yet color-coded, but it should be a modern color that can also be used for a later website. The design should be innovation. Exude dynamism and reliability

Target Market(s)

IT security, IT solutions

Contact Information for Business Card

Firma: brandel-advisory, Inhaber: Jonas Wirtel
Adresse: Lindenhang 4, D-73218 Steinwalden
Telefon: +49 (0) 7354 608193
E-Mail Jonas.Wirtel@brandel-advisory.example

```html
<!DOCTYPE html>
<html lang="de">
<head>
<meta charset="utf-8">
<title>Brandel Advisory – Visitenkarte</title>
<link rel="stylesheet" href="https://fonts.googleapis.com/css2?family=Lato:wght@400;700;900&display=swap">
<style>
  :root {
    --brand-blue: #1279a1;
    --brand-blue-dark: #0f6a8e;
    --card-white: #ffffff;
    --ink: #2b2b2b;
    --rule-grey: #8a8a8a;
    --watermark-grey: #ececec;
    --backdrop: #d9d9d9;
  }
  * { box-sizing: border-box; margin: 0; padding: 0; }
  html, body {
    width: 1200px;
    height: 900px;
    overflow: hidden;
    background: var(--backdrop);
    font-family: "Lato", sans-serif;
  }
  .stage {
    width: 1200px;
    height: 900px;
    display: flex;
    flex-direction: column;
    align-items: center;
    justify-content: center;
    gap: 44px;
  }
  .card {
    position: relative;
    width: 620px;
    height: 354px;
    border-radius: 22px;
    overflow: hidden;
    box-shadow: 0 6px 18px rgba(0,0,0,0.18);
  }

  /* Front */
  .card--front {
    background: var(--brand-blue);
    display: flex;
    flex-direction: column;
    align-items: center;
    justify-content: center;
    color: var(--card-white);
  }
  .brand-mark {
    display: flex;
    flex-direction: column;
    align-items: center;
  }
  .brand-mark__dot {
    width: 58px;
    height: 58px;
    border-radius: 50%;
    border: 7px solid currentColor;
    margin-bottom: 12px;
  }
  .brand-mark__name {
    font-weight: 900;
    font-size: 46px;
    letter-spacing: 2px;
    line-height: 1;
    text-transform: uppercase;
  }
  .brand-mark__tagline {
    display: flex;
    align-items: center;
    gap: 10px;
    margin-top: 6px;
    font-weight: 900;
    font-size: 13px;
    letter-spacing: 5px;
    text-transform: uppercase;
  }
  .brand-mark__rule {
    width: 46px;
    height: 1.5px;
    background: currentColor;
  }

  /* Back */
  .card--back {
    background: var(--card-white);
  }
  .watermark-ring {
    position: absolute;
    right: -120px;
    top: -30px;
    width: 400px;
    height: 400px;
    border-radius: 50%;
    border: 42px solid var(--watermark-grey);
  }
  .back-logo {
    position: absolute;
    left: 40px;
    top: 90px;
    display: flex;
    align-items: center;
    gap: 16px;
    color: var(--brand-blue);
  }
  .back-logo__dot {
    width: 64px;
    height: 64px;
    border-radius: 50%;
    border: 8px solid currentColor;
  }
  .back-logo__text {
    display: flex;
    flex-direction: column;
    align-items: flex-start;
  }
  .back-logo__name {
    font-weight: 900;
    font-size: 38px;
    letter-spacing: 1.5px;
    line-height: 1;
    text-transform: uppercase;
  }
  .back-logo__tagline {
    display: flex;
    align-items: center;
    gap: 8px;
    margin-top: 4px;
    font-weight: 900;
    font-size: 11px;
    letter-spacing: 4px;
    text-transform: uppercase;
  }
  .back-logo__rule {
    width: 30px;
    height: 1.5px;
    background: var(--rule-grey);
  }
  .contact {
    position: absolute;
    left: 40px;
    top: 200px;
    color: var(--ink);
  }
  .contact__name {
    color: var(--brand-blue);
    font-weight: 900;
    font-size: 22px;
    letter-spacing: 0.5px;
    text-transform: uppercase;
  }
  .contact__role {
    font-size: 14px;
    margin-bottom: 10px;
  }
  .contact__line {
    display: flex;
    align-items: center;
    gap: 6px;
    font-size: 16px;
    line-height: 1.4;
  }
  .contact__icon {
    width: 16px;
    height: 16px;
    flex: none;
    color: var(--brand-blue-dark);
  }
  .contact__address {
    font-size: 16px;
    margin-top: 8px;
  }
</style>
</head>
<body>
<main class="stage">
  <section class="card card--front" aria-label="Vorderseite">
    <div class="brand-mark">
      <div class="brand-mark__dot"></div>
      <div class="brand-mark__name">Brandel</div>
      <div class="brand-mark__tagline">
        <span class="brand-mark__rule"></span>Advisory<span class="brand-mark__rule"></span>
      </div>
    </div>
  </section>

  <section class="card card--back" aria-label="Rückseite">
    <div class="watermark-ring"></div>
    <div class="back-logo">
      <div class="back-logo__dot"></div>
      <div class="back-logo__text">
        <div class="back-logo__name">Brandel</div>
        <div class="back-logo__tagline">
          <span class="back-logo__rule"></span>Advisory<span class="back-logo__rule"></span>
        </div>
      </div>
    </div>
    <div class="contact">
      <div class="contact__name">Jonas Wirtel</div>
      <div class="contact__role">Owner</div>
      <div class="contact__line">
        <svg class="contact__icon" viewBox="0 0 16 16" aria-hidden="true">
          <rect x="0.75" y="0.75" width="14.5" height="14.5" rx="2" fill="none" stroke="currentColor" stroke-width="1.5"/>
          <path d="M5 3.5c-.8.3-1.4 1-1.2 2 .5 2.8 3.6 6 6.5 6.6 1 .2 1.7-.4 2-1.2l-1.8-1.3-1 .8c-1.3-.6-2.5-1.8-3.1-3.1l.8-1z" fill="currentColor"/>
        </svg>
        <span>+49 (0) 7354 608193</span>
      </div>
      <div class="contact__line">
        <svg class="contact__icon" viewBox="0 0 16 16" aria-hidden="true">
          <rect x="0.5" y="3" width="15" height="10" fill="currentColor"/>
          <path d="M0.5 3 L8 9 L15.5 3" fill="none" stroke="#fff" stroke-width="1.2"/>
        </svg>
        <span>Jonas.Wirtel@brandel-advisory.example</span>
      </div>
      <div class="contact__address">Lindenhang 4, D-73218 Steinwalden</div>
    </div>
  </section>
</main>
</body>
</html>
```